Frostwyn.co - Polar Expeditions Specialists

We need a modern, visually striking business card for Frostwyn.co, a company specialized in selling expedition cruises to the most remote regions on Earth, with a focus on the Arctic and Antarctica. The design should instantly communicate that the cardholder is an expert in polar travel. Use clean, premium aesthetics with cool tones like icy blue and white, possibly incorporating polar imagery (ice, glaciers, penguins, etc.)

Attached the logo

Contact Information for Business Card

Feels high-end and trustworthy.. Visually memorable — encourages people to keep it

Colors
0054AA
0677BA
7BADD7
CADEEF
E8F1F8

Requirements
Must have
• ice, glaciers, penguins, montains
Nice to have
• modern, transparente,

```html
<!DOCTYPE html>
<html lang="en">
<head>
<meta charset="UTF-8">
<title>Frostwyn.co – Business Card</title>
<link rel="stylesheet" href="https://fonts.googleapis.com/css2?family=Poppins:wght@300;400;600;700&display=swap">
<style>
  :root {
    --page-bg: #e6ecf1;
    --card-edge: #d6e0e8;
    --brand-blue: #3b68a8;
    --ink: #111417;
    --ink-soft: #3a3f45;
    --divider: #5a5f66;
    --sky: #dfe6ec;
    --ice-light: #eef3f6;
    --ice-mid: #d3dee5;
    --water: #b4c3cb;
    --water-deep: #9fb0ba;
  }
  * { margin: 0; padding: 0; box-sizing: border-box; }
  html, body {
    width: 1200px;
    height: 900px;
    overflow: hidden;
    background: var(--page-bg);
    font-family: "Poppins", sans-serif;
  }
  .card {
    position: absolute;
    left: 120px;
    top: 176px;
    width: 960px;
    height: 548px;
    border: 1px solid var(--card-edge);
    box-shadow: 0 18px 40px rgba(40, 70, 100, 0.12);
    overflow: hidden;
  }
  .card-scene {
    position: absolute;
    inset: 0;
    background:
      radial-gradient(ellipse 420px 260px at 230px 400px, var(--ice-light) 0%, rgba(238,243,246,0) 100%),
      radial-gradient(ellipse 380px 160px at 820px 470px, var(--ice-light) 0%, rgba(238,243,246,0) 100%),
      linear-gradient(180deg, var(--sky) 0%, var(--sky) 34%, var(--ice-mid) 56%, var(--ice-light) 74%, var(--water) 86%, var(--water-deep) 100%);
  }
  .card-frost {
    position: absolute;
    inset: 0;
    background: rgba(244, 247, 250, 0.35);
  }
  .brand {
    position: absolute;
    left: 61px;
    width: 400px;
    top: 152px;
    text-align: center;
    color: var(--brand-blue);
  }
  .brand-mark {
    width: 110px;
    height: 110px;
    margin: 0 auto 26px;
    border-radius: 50%;
    background: var(--brand-blue);
  }
  .brand-name {
    font-size: 58px;
    font-weight: 700;
    line-height: 1;
    letter-spacing: -0.5px;
  }
  .brand-tagline {
    margin-top: 14px;
    font-size: 19px;
    font-weight: 600;
    line-height: 1;
  }
  .divider {
    position: absolute;
    left: 480px;
    top: 150px;
    width: 2px;
    height: 247px;
    background: var(--divider);
  }
  .contact {
    position: absolute;
    left: 554px;
    top: 168px;
  }
  .holder-name {
    font-size: 31px;
    font-weight: 700;
    color: var(--ink);
    line-height: 1;
  }
  .holder-position {
    margin-top: 14px;
    font-size: 18px;
    font-weight: 400;
    letter-spacing: 3.5px;
    color: var(--brand-blue);
    line-height: 1;
  }
  .contact-list {
    list-style: none;
    margin-top: 29px;
  }
  .contact-item {
    display: flex;
    align-items: center;
    height: 37px;
    font-size: 24px;
    font-weight: 300;
    color: var(--ink-soft);
  }
  .contact-icon {
    width: 20px;
    height: 20px;
    margin-right: 14px;
    fill: var(--brand-blue);
    flex: none;
  }
</style>
</head>
<body>
  <div class="card">
    <div class="card-scene" role="img" aria-label="Glaciers, icebergs and polar sea seen through the transparent card"></div>
    <div class="card-frost"></div>

    <div class="brand">
      <div class="brand-mark"></div>
      <div class="brand-name">Frostwyn.co</div>
      <div class="brand-tagline">Polar Expeditions Specialists</div>
    </div>

    <div class="divider"></div>

    <div class="contact">
      <div class="holder-name">NAME SURNAME</div>
      <div class="holder-position">POSITION</div>
      <ul class="contact-list">
        <li class="contact-item">
          <svg class="contact-icon" viewBox="0 0 20 20" aria-hidden="true">
            <path d="M5 1h10a1.5 1.5 0 0 1 1.5 1.5v15A1.5 1.5 0 0 1 15 19H5a1.5 1.5 0 0 1-1.5-1.5v-15A1.5 1.5 0 0 1 5 1zm.5 2.5v11h9v-11zM10 15.6a1.1 1.1 0 1 0 0 2.2 1.1 1.1 0 0 0 0-2.2z"/>
          </svg>
          (123) 456-7890
        </li>
        <li class="contact-item">
          <svg class="contact-icon" viewBox="0 0 20 20" aria-hidden="true">
            <path d="M1.5 4h17v12h-17zM3 5.6v.4l7 5 7-5v-.4zm0 2.2v6.7h14V7.8l-7 5z"/>
          </svg>
          name@website.com
        </li>
        <li class="contact-item">
          <svg class="contact-icon" viewBox="0 0 20 20" aria-hidden="true">
            <path d="M10 2a8 8 0 1 0 0 16 8 8 0 0 0 0-16zm5.9 7h-2.6a12 12 0 0 0-1-4.6A6.5 6.5 0 0 1 15.9 9zM10 3.6c.8 1 1.6 3 1.8 5.4H8.2C8.4 6.6 9.2 4.6 10 3.6zM7.7 4.4A12 12 0 0 0 6.7 9H4.1a6.5 6.5 0 0 1 3.6-4.6zM4.1 11h2.6a12 12 0 0 0 1 4.6A6.5 6.5 0 0 1 4.1 11zm5.9 5.4c-.8-1-1.6-3-1.8-5.4h3.6c-.2 2.4-1 4.4-1.8 5.4zm2.3-.8a12 12 0 0 0 1-4.6h2.6a6.5 6.5 0 0 1-3.6 4.6z"/>
          </svg>
          website.com
        </li>
      </ul>
    </div>
  </div>
</body>
</html>
```